Postcard Design

We are a pet resort located near Atlanta's Corbinvale Pruett Airport. I want a postcard that will show dogs playing and the offer will be "New customers receive 50% off boarding" *
* 50% offer applies to standard lodging fees only. Amenities and playtimes not included in this offer. Valid for up to 10 nights of boarding. Blackout dates of July 4th, Thanksgiving week and Christmas week apply. Reservations required.
The backside of the postcard will read, "New daycare customers recieve ONE WEEK of FREE daycare for your dog".*
* offer good for 5 consecutive days of daycare only-not in conjuction with overnight lodging. Good for one pet per family only. Offer not valid on July 4th week, Thanksgiving week or Christmas week.

```html
<!DOCTYPE html>
<html lang="en">
<head>
<meta charset="utf-8">
<title>Daycare Offer – Postcard Back</title>
<link rel="stylesheet" href="https://fonts.googleapis.com/css2?family=Cabin:ital,wght@0,400;1,700&family=Arimo:ital,wght@0,400;0,700;1,400&display=swap">
<style>
  :root {
    --paper: #ffffff;
    --ink: #000000;
    --burst-ink: #ffffff;
  }
  html, body {
    margin: 0;
    padding: 0;
    overflow: hidden;
    background: var(--paper);
  }
  .postcard {
    position: relative;
    width: 1200px;
    height: 931px;
    background: var(--paper);
    color: var(--ink);
    overflow: hidden;
  }
  .burst {
    position: absolute;
    left: 0;
    top: 0;
    width: 400px;
    height: 320px;
  }
  .burst-figure { font-family: "Arimo", Arial, sans-serif; font-weight: 700; fill: var(--burst-ink); }
  .headline {
    position: absolute;
    font-family: "Cabin", "Gill Sans", sans-serif;
    font-size: 26px;
    line-height: 1;
    margin: 0;
    white-space: nowrap;
  }
  .headline em { font-style: italic; font-weight: 700; }
  .headline-1 { left: 70px; top: 47px; }
  .headline-2 { left: 238px; top: 83px; }
  .headline-3 { left: 247px; top: 120px; }
  .terms {
    position: absolute;
    left: 54px;
    margin: 0;
    font-family: "Arimo", Arial, sans-serif;
  }
  .terms-limit { top: 323px; font-size: 24px; font-weight: 700; line-height: 33px; }
  .terms-eligibility { top: 453px; font-size: 24px; line-height: 31px; }
  .terms-blackout { top: 645px; font-size: 28px; line-height: 36px; }
  .terms-blackout em { font-style: italic; }
</style>
</head>
<body>
<main class="postcard">
  <svg class="burst" viewBox="0 0 400 320" aria-hidden="true">
    <polygon fill="#000"
      points="42,153 140,150 120,128 158,135 172,85 195,132 240,112 242,152 300,168 262,190 325,202 270,225 368,265 250,250 210,295 188,257 95,262 140,232 58,218 118,200 70,186 125,176"/>
    <g transform="rotate(-7 210 205)">
      <text class="burst-figure" x="152" y="226" font-size="62">50</text>
      <text class="burst-figure" x="252" y="196" font-size="18">%</text>
      <text class="burst-figure" x="172" y="242" font-size="14">off lodging</text>
      <text class="burst-figure" x="200" y="256" font-size="14">fees!</text>
    </g>
  </svg>

  <p class="headline headline-1"><em>New daycare customers</em> receive</p>
  <p class="headline headline-2">ONE WEEK of FREE</p>
  <p class="headline headline-3">daycare for your dog!</p>

  <p class="terms terms-limit">Offer good for 5 consecutive days<br>of daycare only!</p>
  <p class="terms terms-eligibility">Not in conjuction<br>with overnight lodging.<br>Good for one pet<br>per family only.</p>
  <p class="terms terms-blackout">Offer not valid<br>on <em>July 4th week,</em><br><em>Thanksgiving week or Christmas week.</em></p>
</main>
</body>
</html>
```